Business card design needed

Bright Path Ahead is an online wellness program designed for people dealing with cancer to take control of their lives and bright path ahead.

Target Market(s)

initially woman aged 35 to 65 years eventaully then men

Industry/Entity Type

Business

Contact Information for Business Card

Marlena Throsby
Bright path ahead Coach
Marlena@brightpathway.com.au
M 0418392716
Skype Marlena.Throsby
local number to come
www.brightpathway.com.au

Requirements
Must have
• Business cards want to have a photo of me on the back this is a head shot. Also a small blurb " Marlena recovered and survived 2 types of cancer. She under went a transformational 12 month journey to overcome cancer naturally . Join her online coaching program to bright path ahead.

Phone number and email and skype address.
Nice to have
• Looking for something that resembles health EG abstract tree of life, or something resembling health and balance . Like lime green/apple green want modern fresh. Want only 2 colours used on the cards. Need to use the logo and Bright path ahead on website and email signature - Clean and fresh

Also would like Letter head and logo for website and email signature

```html
<!DOCTYPE html>
<html lang="en">
<head>
<meta charset="utf-8">
<title>Bright Path Ahead – Business Card</title>
<link rel="stylesheet" href="https://fonts.googleapis.com/css2?family=Questrial&display=swap">
<style>
  :root {
    --stage: #3b3c40;
    --blue-deep: #1550b0;
    --blue: #1f6fc8;
    --blue-light: #3a93dc;
    --silver: #e4e5e7;
    --silver-dark: #c9cacd;
    --card-grey: #dcdcdc;
    --ink: #1e1e22;
    --white: #ffffff;
    --photo-front: #9aa3a6;
    --photo-teal: #2e8b8f;
  }
  * { box-sizing: border-box; margin: 0; padding: 0; }
  html, body { width: 1200px; height: 900px; overflow: hidden; }
  body {
    background: var(--stage);
    font-family: "Questrial", "Century Gothic", sans-serif;
    position: relative;
  }
  .presentation-title {
    position: absolute; top: 36px; right: 48px;
    font-size: 48px; color: var(--white); font-weight: 400;
  }
  .card {
    position: absolute; left: 200px; width: 640px; height: 366px;
    overflow: hidden; box-shadow: 0 6px 18px rgba(0,0,0,.45);
  }
  /* Front */
  .card-front { top: 120px; background: linear-gradient(90deg, var(--blue) 0%, var(--blue-light) 38%, #b9c8d6 58%, var(--card-grey) 70%); }
  .front-photo {
    position: absolute; right: 0; top: 0; width: 300px; height: 100%;
    background: radial-gradient(ellipse at 45% 55%, var(--photo-teal) 0%, var(--photo-front) 45%, #c7c9cb 80%);
    opacity: .85;
    -webkit-mask-image: linear-gradient(90deg, transparent 0, #000 70px);
            mask-image: linear-gradient(90deg, transparent 0, #000 70px);
  }
  .brand {
    position: absolute; left: 90px; top: 52px;
    display: flex; align-items: center; gap: 10px;
    color: var(--white); font-size: 30px; letter-spacing: 1px;
  }
  .brand-dot { width: 16px; height: 16px; border-radius: 50%; background: var(--white); }
  .name-band {
    position: absolute; left: 0; top: 132px; width: 100%; height: 52px;
    background: linear-gradient(90deg, var(--silver) 0%, var(--silver) 50%, rgba(228,229,231,0) 80%);
    padding: 8px 0 0 80px; color: var(--ink);
  }
  .person-name { font-size: 22px; line-height: 1.05; }
  .person-role { font-size: 13px; }
  .contact-list {
    position: absolute; left: 80px; top: 200px; list-style: none;
    color: var(--white); font-size: 17px; line-height: 23px;
  }
  .contact-list li { display: flex; align-items: center; gap: 8px; }
  .contact-list svg { width: 13px; height: 13px; fill: var(--white); flex: none; }
  /* Back */
  .card-back { top: 510px; background: linear-gradient(180deg, #e2e2e2 0%, var(--card-grey) 100%); }
  .back-photo {
    position: absolute; right: 0; top: 0; width: 290px; height: 270px;
    background: radial-gradient(ellipse at 40% 40%, #d7b9a3 0%, #bfa894 30%, #cdd0d1 70%, #e0e0e0 100%);
    -webkit-mask-image: linear-gradient(90deg, transparent 0, #000 60px);
            mask-image: linear-gradient(90deg, transparent 0, #000 60px);
  }
  .blurb {
    position: absolute; right: 310px; top: 40px; width: 300px;
    text-align: right; color: var(--ink); font-size: 16px; line-height: 20px;
  }
  .blurb p + p { margin-top: 18px; }
  .web-band {
    position: absolute; left: 0; bottom: 0; width: 100%; height: 96px;
    background: linear-gradient(90deg, var(--blue-deep) 0%, var(--blue) 55%, var(--blue-light) 100%);
    color: var(--white); font-size: 36px;
    display: flex; align-items: center; padding-left: 120px;
  }
</style>
</head>
<body>
  <h1 class="presentation-title">Bright path ahead</h1>

  <section class="card card-front" aria-label="Card front">
    <div class="front-photo" role="img" aria-label="Photo of the coach seated, wearing a teal top and beaded necklace"></div>
    <div class="brand"><span class="brand-dot"></span><span>Bright Path Ahead</span></div>
    <div class="name-band">
      <div class="person-name">Marlena Throsby</div>
      <div class="person-role">Bright path ahead Coach</div>
    </div>
    <ul class="contact-list">
      <li><svg viewBox="0 0 16 16"><path d="M1 3h14v10H1z M1 3l7 6 7-6" fill="none" stroke="#fff" stroke-width="1.6"/></svg>Marlena@brightpathway.com.au</li>
      <li><svg viewBox="0 0 16 16"><rect x="4" y="1" width="8" height="14" rx="1.5"/></svg>0418392716</li>
      <li><svg viewBox="0 0 16 16"><circle cx="8" cy="8" r="7"/></svg>4521098837</li>
      <li><svg viewBox="0 0 16 16"><rect x="1" y="1" width="14" height="14" rx="3"/></svg>Marlena.Throsby</li>
    </ul>
  </section>

  <section class="card card-back" aria-label="Card back">
    <div class="back-photo" role="img" aria-label="Head shot of the coach resting her chin on her hand"></div>
    <div class="blurb">
      <p>Marlena recovered and<br>survived 2 types of cancer.</p>
      <p>She under went<br>a transformational 12 month journey<br>to overcome cancer naturally.</p>
      <p>Join her online coaching program<br>to bright path ahead.</p>
    </div>
    <div class="web-band">www.brightpathway.com.au</div>
  </section>
</body>
</html>
```